Marrow Lantern - a Thriller Novel

A thriller set in Antarctica. I'm envisioning an image of the entire continent as viewed from above, white and icy and surrounded by stormy seas if you can tell that much, but the entire continent filled with a colorful cymatic image (if you Google image these you'll see what I mean -- any pattern will do if it looks right, and if it's royalty-free). An alternative: icy white scene viewed from the front like normal, with the colorful cymatic image on top.
Title is "Marrow Lantern". Author is J.R. Pellow
Here's one cymatic image: https://www.plimsearch-example.net/imgres?q=cymatic%20images&imgurl=https%3A%2F%2Fvortelhall-example.org%2Fuploads%2F2017%2F05%2FPattern_Plate3.jpg&imgrefurl=https%3A%2F%2Fvortelhall-example.org%2Fexhibits%2Fpatterns-in-sound&docid=Qz7Hk2LmPa9XcV&tbnid=Rt4NwYb8JsEdKq&vet=12ahUKEwXyZbQmTqPlRwTnKsLDfP9rWuHqN2aFDCcQBB..i&w=900&h=560
Here's a bunch more: https://www.plimsearch-example.net/imgres?q=cymatic%20images&imgurl=https%3A%2F%2Ftolbrik-example.org%2Fuploads%2F2023%2F03%2FPattern-Sheet.jpg&imgrefurl=https%3A%2F%2Ftolbrik-example.org%2Fpatterns%2F&docid=Lp3VxRt8NmKwQe&tbnid=Hy6JdPs2WqZcBn&vet=12ahUKEwXyZbQmTqPlRwTnKsLDfP9rWuHqN2aFDDmRCC..i&w=866&h=835
But of course, something royalty-free or similar. I believe they are all circular fractal patterns, for whatever that's worth.
new adult, adult

```html
<!DOCTYPE html>
<html lang="en">
<head>
<meta charset="utf-8">
<title>Marrow Lantern — J.R. Pellow</title>
<link rel="stylesheet" href="https://fonts.googleapis.com/css2?family=Bebas+Neue&family=Allura&display=swap">
<style>
  :root {
    --backdrop: #1a1b1a;
    --ice-light: #f1f3f5;
    --ice-shade: #e2e6ea;
    --script-ink: #141414;
    --author-ink: #3b1763;
    --pour-orange: #ee5a1c;
    --pour-red: #c8182c;
    --pour-brown: #3a1810;
    --pour-magenta: #d81f7c;
    --pour-purple: #5b2b94;
    --pour-blue: #2f62d6;
  }

  * { margin: 0; padding: 0; box-sizing: border-box; }

  html, body {
    width: 1200px;
    height: 800px;
    overflow: hidden;
    background: var(--backdrop);
  }

  .canvas {
    position: relative;
    width: 1200px;
    height: 800px;
  }

  .book-cover {
    position: absolute;
    left: 366px;
    top: 40px;
    width: 468px;
    height: 720px;
    display: block;
  }

  .ice-field-top { stop-color: var(--ice-light); }
  .ice-field-bottom { stop-color: var(--ice-shade); }

  .title-heavy {
    font-family: "Bebas Neue", "Arial Narrow", sans-serif;
  }

  .title-script {
    font-family: "Allura", cursive;
    font-size: 122px;
    fill: var(--script-ink);
  }

  .author-name {
    font-family: "Bebas Neue", "Arial Narrow", sans-serif;
    font-size: 40px;
    letter-spacing: 0.5px;
    fill: var(--author-ink);
  }

  .pour-orange { stop-color: var(--pour-orange); }
  .pour-red { stop-color: var(--pour-red); }
  .pour-brown { stop-color: var(--pour-brown); }
  .pour-magenta { stop-color: var(--pour-magenta); }
  .pour-purple { stop-color: var(--pour-purple); }
  .pour-blue { stop-color: var(--pour-blue); }
</style>
</head>
<body>
  <main class="canvas">
    <svg class="book-cover" viewBox="0 0 468 720" xmlns="http://www.w3.org/2000/svg">
      <defs>
        <linearGradient id="ice-field" x1="0" y1="0" x2="0.3" y2="1">
          <stop offset="0" class="ice-field-top"/>
          <stop offset="1" class="ice-field-bottom"/>
        </linearGradient>

        <linearGradient id="pour-base" x1="0" y1="0" x2="1" y2="1">
          <stop offset="0" class="pour-orange"/>
          <stop offset="0.3" class="pour-brown"/>
          <stop offset="0.5" class="pour-purple"/>
          <stop offset="0.7" class="pour-magenta"/>
          <stop offset="1" class="pour-red"/>
        </linearGradient>

        <radialGradient id="pour-ring-left" cx="0.5" cy="0.5" r="0.5">
          <stop offset="0" class="pour-orange"/>
          <stop offset="0.55" class="pour-red" stop-opacity="0.8"/>
          <stop offset="1" class="pour-red" stop-opacity="0"/>
        </radialGradient>

        <radialGradient id="pour-ring-centre" cx="0.5" cy="0.5" r="0.5">
          <stop offset="0" class="pour-blue"/>
          <stop offset="0.5" class="pour-purple" stop-opacity="0.8"/>
          <stop offset="1" class="pour-purple" stop-opacity="0"/>
        </radialGradient>

        <radialGradient id="pour-ring-right" cx="0.5" cy="0.5" r="0.5">
          <stop offset="0" class="pour-magenta"/>
          <stop offset="0.6" class="pour-magenta" stop-opacity="0.7"/>
          <stop offset="1" class="pour-magenta" stop-opacity="0"/>
        </radialGradient>

        <clipPath id="title-letters">
          <text class="title-heavy" x="82" y="313" font-size="261" textLength="314" lengthAdjust="spacing">MAR</text>
          <text class="title-heavy" x="82" y="475" font-size="221" textLength="314" lengthAdjust="spacing">ROW</text>
        </clipPath>
      </defs>

      <rect class="ice-field" width="468" height="720" fill="url(#ice-field)"
            role="img" aria-label="Icy white Antarctic field"/>

      <g class="title-fill" clip-path="url(#title-letters)" role="img"
         aria-label="MARROW in heavy condensed capitals filled with a colourful circular cymatic pattern">
        <rect x="70" y="120" width="340" height="370" fill="url(#pour-base)"/>
        <circle cx="140" cy="230" r="120" fill="url(#pour-ring-left)"/>
        <circle cx="250" cy="350" r="110" fill="url(#pour-ring-centre)"/>
        <circle cx="360" cy="220" r="110" fill="url(#pour-ring-right)"/>
        <circle cx="120" cy="430" r="90" fill="url(#pour-ring-left)"/>
        <circle cx="370" cy="430" r="90" fill="url(#pour-ring-right)"/>
      </g>

      <text class="title-script" x="92" y="556">Lantern</text>

      <text class="author-name" x="386" y="631" text-anchor="end">J.R. PELLOW</text>
    </svg>
  </main>
</body>
</html>
```